Full service residential and commercial painting
Finest quality attention to detail
All workmanship guaranteed
Email :norabvantreel@mailbox-example.fr
Mobile: 0417382650
Industry/Entity Type
Residential
Contact Information for Business Card
Henri marsot painting & decorating
Requirements
Nice to have
- Am thinking about someone can be painting my name on the card with HM painting with the logos of brush,pot tray and roller sleeves

```html
<!DOCTYPE html>
<html lang="en">
<head>
<meta charset="utf-8">
<title>Henri Marsot Painting &amp; Decorating – Business Card</title>
<link rel="stylesheet" href="https://fonts.googleapis.com/css2?family=Cabin+Sketch:wght@700&family=PT+Sans:wght@400&display=swap">
<style>
  :root {
    --stage-light: #ffffff;
    --stage-dark: #d6d6d6;
    --card: #333333;
    --paint-red: #e83236;
    --paint-red-fade: rgba(232, 50, 54, 0);
    --text-white: #ffffff;
  }
  * { margin: 0; padding: 0; box-sizing: border-box; }
  html, body { width: 1200px; height: 1000px; overflow: hidden; }
  body {
    position: relative;
    background: radial-gradient(ellipse at center, var(--stage-light) 45%, var(--stage-dark) 100%);
    font-family: "PT Sans", Arial, sans-serif;
  }
  .card {
    position: absolute;
    left: 68px; top: 161px;
    width: 1050px; height: 675px;
    background: var(--card);
    overflow: hidden;
  }
  .splatter {
    position: absolute;
    width: 180px; height: 170px;
  }
  .splatter--tl { left: 0; top: 0;
    background: radial-gradient(ellipse 175px 165px at 0 0, var(--paint-red) 45%, var(--paint-red-fade) 100%); }
  .splatter--tr { right: 0; top: 0;
    background: radial-gradient(ellipse 175px 165px at 100% 0, var(--paint-red) 45%, var(--paint-red-fade) 100%); }
  .splatter--bl { left: 0; bottom: 0;
    background: radial-gradient(ellipse 175px 165px at 0 100%, var(--paint-red) 45%, var(--paint-red-fade) 100%); }
  .splatter--br { right: 0; bottom: 0;
    background: radial-gradient(ellipse 175px 165px at 100% 100%, var(--paint-red) 45%, var(--paint-red-fade) 100%); }
  .tagline {
    position: absolute;
    top: 14px; left: 0; width: 100%;
    text-align: center;
    color: var(--text-white);
    font-size: 29px;
    line-height: 35px;
    padding-left: 36px;
  }
  .brand {
    position: absolute;
    top: 276px; left: 0; width: 100%;
    text-align: center;
    padding-right: 16px;
  }
  .brand__name {
    font-family: "Cabin Sketch", "Comic Sans MS", cursive;
    font-weight: 700;
    font-size: 84px;
    line-height: 90px;
    color: var(--text-white);
    letter-spacing: 3px;
    text-transform: uppercase;
  }
  .brand__trade {
    font-size: 52px;
    line-height: 58px;
    color: var(--paint-red);
  }
  .contact {
    position: absolute;
    bottom: 8px; left: 0; width: 100%;
    display: flex;
    justify-content: center;
    gap: 40px;
    color: var(--text-white);
    font-size: 24px;
    line-height: 34px;
  }
</style>
</head>
<body>
  <main class="card">
    <div class="splatter splatter--tl" role="img" aria-label="Red paint splatter in the corner"></div>
    <div class="splatter splatter--tr" role="img" aria-label="Red paint splatter in the corner"></div>
    <div class="splatter splatter--bl" role="img" aria-label="Red paint splatter in the corner"></div>
    <div class="splatter splatter--br" role="img" aria-label="Red paint splatter in the corner"></div>

    <p class="tagline">Full service residential and commercial painting.<br>Finest quality attention to detail. All workmanship guaranteed.</p>

    <header class="brand">
      <h1 class="brand__name">Henri Marsot</h1>
      <p class="brand__trade">Painting &amp; Decorating</p>
    </header>

    <footer class="contact">
      <span class="contact__email">Email :norabvantreel@mailbox-example.fr</span>
      <span class="contact__mobile">Mobile: 0417382650</span>
    </footer>
  </main>
</body>
</html>
```